Restaurant Posters

Looking for two posters to be created for restaurant promos - see below for details:

Design #1 -
Want to highlight two main specials we offer - first is Tuesday BOGO Burgers (with purchase of two beverages), second is on Wednesday's we offer $0.75 Wings (includes traditional and boneless) and $2 off IPA's

Then at the bottom smaller would like to call out two less important offers - first is $2 off Nebraska Beers on Mondays, and the second is 1/2 off 19.2oz Crowlers on Thursdays

Design #2 -
Looking to create a sign up for our e-club and receive a free appetizer upon sign up, free burger on your birthday week, and access to exclusive deals and email offers

See attached for supporting docs you may use - don't have to but feel free to get creative with these. Would like the designs to be simple, and follow our brand look and feel as much as possible. Our website is not a good indication of our brand - I would go more off of our logos, and our menu design.

Need extra days to review

```html
<!DOCTYPE html>
<html lang="en">
<head>
<meta charset="utf-8">
<title>Prairie Tap House – Weekly Specials Poster</title>
<link rel="stylesheet" href="https://fonts.googleapis.com/css2?family=Oswald:wght@500;700&display=swap">
<style>
  :root {
    --page-bg: #efe7dc;
    --poster-red: #d91f26;
    --poster-red-deep: #b5161c;
    --poster-orange: #f7931e;
    --poster-amber: #f6a93b;
    --ink-dark: #3b3a3a;
    --text-light: #ffffff;
    --chip-light: #f4f1ee;
    --photo-burger: #c98a4b;
    --photo-burger-light: #f1dcc0;
    --photo-wings: #c7361d;
    --photo-wings-green: #6aa53a;
  }
  * { box-sizing: border-box; margin: 0; padding: 0; }
  html, body {
    width: 1200px; height: 1200px; overflow: hidden;
    background: var(--page-bg);
    font-family: "Oswald", "Arial Narrow", sans-serif;
  }
  .poster {
    position: absolute; left: 180px; top: 40px;
    width: 840px; height: 1120px; overflow: hidden;
    background: radial-gradient(circle at 51% 58%, var(--poster-amber) 0%, var(--poster-orange) 22%, var(--poster-red) 62%, var(--poster-red-deep) 100%);
    color: var(--text-light);
  }
  .special-title {
    position: absolute; font-weight: 700; line-height: 1;
    text-shadow: 0 2px 3px rgba(0,0,0,.25);
  }
  .special-note { position: absolute; font-weight: 500; line-height: 1.15; }
  .special-day {
    position: absolute; font-weight: 700; font-size: 24px; line-height: 1;
    letter-spacing: 2px; text-transform: uppercase;
  }
  .burger-title { left: 80px; top: 88px; font-size: 46px; }
  .burger-note { left: 82px; top: 145px; font-size: 25px; }
  .photo {
    position: absolute; background: #fff; padding: 10px;
    box-shadow: 0 3px 8px rgba(0,0,0,.25);
  }
  .photo-fill { width: 100%; height: 100%; }
  .photo-burger { left: 100px; top: 190px; width: 290px; height: 290px; }
  .photo-burger .photo-fill {
    background: radial-gradient(ellipse at 50% 55%, var(--photo-burger) 0%, var(--photo-burger) 38%, var(--photo-burger-light) 72%, #fff 100%);
  }
  .photo-wings { left: 420px; top: 168px; width: 370px; height: 205px; }
  .photo-wings .photo-fill {
    background: radial-gradient(ellipse at 45% 50%, var(--photo-wings) 0%, var(--photo-wings) 34%, var(--photo-wings-green) 58%, #fff 90%);
  }
  .wings-day { left: 442px; top: 392px; }
  .wings-title { left: 440px; top: 422px; font-size: 46px; }
  .wings-note { left: 442px; top: 478px; font-size: 25px; }
  .brand-mark {
    position: absolute; left: 345px; top: 570px;
    width: 150px; height: 150px; border-radius: 50%;
    background: var(--ink-dark);
  }
  .brand-name {
    position: absolute; left: 0; right: 0; text-align: center;
    color: var(--ink-dark); font-weight: 700; line-height: 1;
  }
  .brand-name-main { top: 735px; font-size: 86px; letter-spacing: 2px; }
  .brand-name-sub { top: 830px; font-size: 30px; letter-spacing: 6px; }
  .minor-offers {
    position: absolute; left: 70px; right: 70px; top: 895px;
    display: flex; justify-content: space-between;
  }
  .minor-offer { width: 335px; line-height: 1.1; }
  .minor-offer-day {
    font-weight: 700; font-size: 20px; letter-spacing: 2px; text-transform: uppercase;
  }
  .minor-offer-text { font-weight: 500; font-size: 26px; }
  .contact {
    position: absolute; top: 1030px; display: flex; align-items: center; gap: 12px;
    font-weight: 500; font-size: 18px; line-height: 1.2;
  }
  .contact-address { left: 70px; }
  .contact-web { left: 370px; }
  .globe-badge {
    width: 36px; height: 36px; border-radius: 50%; background: var(--chip-light);
    display: flex; align-items: center; justify-content: center;
  }
  .social-links {
    position: absolute; left: 626px; top: 1035px; display: flex; gap: 12px;
  }
  .social-square { width: 40px; height: 40px; border-radius: 6px; background: var(--chip-light); }
</style>
</head>
<body>
  <main class="poster">
    <h1 class="special-title burger-title">Tuesday BOGO Burgers</h1>
    <p class="special-note burger-note">(with purchase of two beverages)</p>

    <figure class="photo photo-burger">
      <div class="photo-fill" role="img" aria-label="Photo of a stacked burger with cheese, lettuce and tomato"></div>
    </figure>
    <figure class="photo photo-wings">
      <div class="photo-fill" role="img" aria-label="Photo of a bowl of sauced chicken wings with fresh herbs and lime"></div>
    </figure>

    <p class="special-day wings-day">Wednesday</p>
    <h2 class="special-title wings-title">$0.75 Wings</h2>
    <p class="special-note wings-note">(includes traditional and boneless)<br>and $2 off IPA's</p>

    <div class="brand-mark" aria-hidden="true"></div>
    <p class="brand-name brand-name-main">PRAIRIE</p>
    <p class="brand-name brand-name-sub">TAP HOUSE</p>

    <section class="minor-offers">
      <div class="minor-offer">
        <p class="minor-offer-day">Monday</p>
        <p class="minor-offer-text">$2 off Nebraska Beers</p>
      </div>
      <div class="minor-offer">
        <p class="minor-offer-day">Thursday</p>
        <p class="minor-offer-text">1/2 off 19.2oz Crowlers</p>
      </div>
    </section>

    <div class="contact contact-address">
      <svg width="28" height="40" viewBox="0 0 28 40" aria-hidden="true">
        <path d="M14 0C6.3 0 0 6.2 0 13.9 0 24.3 14 40 14 40s14-15.7 14-26.1C28 6.2 21.7 0 14 0z" fill="#3b3a3a"/>
        <circle cx="14" cy="13.5" r="5.5" fill="#f7931e"/>
      </svg>
      <span>Address: Lorem ipsum is<br>placeholder text commonly</span>
    </div>

    <div class="contact contact-web">
      <span class="globe-badge">
        <svg width="22" height="22" viewBox="0 0 24 24" aria-hidden="true" fill="none" stroke="#3b3a3a" stroke-width="2">
          <circle cx="12" cy="12" r="10"/>
          <ellipse cx="12" cy="12" rx="4.5" ry="10"/>
          <line x1="2" y1="12" x2="22" y2="12"/>
        </svg>
      </span>
      <span>www.prairietap.com</span>
    </div>

    <div class="social-links" aria-label="Social media">
      <span class="social-square"></span>
      <span class="social-square"></span>
      <span class="social-square"></span>
    </div>
  </main>
</body>
</html>
```